Poster Design Project for Over 50's Gym

We need a poster design to advertise our over 50's gym. We want to attract older adults who love enjoying their age, living life and having a bit of fun.
We would like to see a bright, fun, non-intimidating poster communicating how easy exercise can be and how great it can be for your health.
I would like the poster to include the following information.
Title:
Mackay's Over 50's Gym
Exercise with confidence
How old would you be if you didn't know your age?
Suitable exercise programmes for all medical conditions
Friendly and non-intimidating environment
Private health insurance rebates
University qualified exercise physiologists
Vital Steps Exercise Physiology Clinic
Exercise Physiologists Danielle Prewitt & Tobias Lindqvist
Suite 7, 245 Corrigan Road, Mackay
www.tullarowvital.com.au
MON - FRI 8:30 am - 6:30 pm
I have photos available for use & Logo just unable to attach at moment****

```html
<!DOCTYPE html>
<html lang="en">
<head>
<meta charset="utf-8">
<title>Mackay's Over 50's Gym – Vital Steps Exercise Physiology Clinic</title>
<link rel="stylesheet" href="https://fonts.googleapis.com/css2?family=Roboto+Condensed:wght@400;700&family=Open+Sans:wght@400;600;700&display=swap">
<style>
  :root {
    --navy: #233a75;
    --orange: #ee6a24;
    --yellow: #f9b934;
    --white: #ffffff;
    --ink: #111111;
  }
  * { margin: 0; padding: 0; box-sizing: border-box; }
  html, body { width: 900px; height: 1200px; overflow: hidden; background: var(--white); }
  .poster {
    position: relative; width: 900px; height: 1200px; overflow: hidden;
    font-family: "Open Sans", sans-serif; background: var(--navy);
  }
  .poster-shapes, .client-photo { position: absolute; inset: 0; }
  .brand {
    position: absolute; left: 222px; top: 44px;
    display: flex; align-items: center; gap: 18px;
  }
  .brand-dot { width: 70px; height: 70px; border-radius: 50%; background: var(--orange); flex: none; }
  .brand-name {
    font-family: "Open Sans", sans-serif; font-weight: 700; color: var(--navy);
    font-size: 30px; line-height: 1.15;
  }
  .clinic-address {
    position: absolute; left: 322px; top: 152px;
    font-size: 19px; line-height: 24px; color: var(--ink); font-family: "Roboto Condensed", sans-serif;
  }
  .clinic-web {
    position: absolute; left: 322px; top: 178px;
    font-size: 18px; line-height: 24px; font-weight: 700; color: var(--navy); letter-spacing: 0.5px;
  }
  .headline {
    position: absolute; left: 0; width: 900px; top: 296px; text-align: center;
    font-family: "Roboto Condensed", sans-serif; font-weight: 700;
    font-size: 66px; line-height: 80px; color: var(--yellow); letter-spacing: 0.5px;
  }
  .bubble-text {
    position: absolute; left: 92px; top: 465px; width: 210px; text-align: center;
    font-family: "Roboto Condensed", sans-serif; font-weight: 700;
    font-size: 37px; line-height: 42px; color: var(--navy);
  }
  .question {
    position: absolute; left: 356px; top: 428px;
    font-family: "Roboto Condensed", sans-serif; font-weight: 700;
    font-size: 28px; line-height: 40px; color: var(--white);
  }
  .benefits { position: absolute; left: 356px; top: 525px; list-style: none; }
  .benefits li {
    display: flex; align-items: center; gap: 12px;
    font-family: "Roboto Condensed", sans-serif; font-size: 18px;
    color: var(--white); height: 29px;
  }
  .benefits li::before {
    content: ""; width: 17px; height: 17px; border-radius: 50%; flex: none;
    background: radial-gradient(circle at 35% 35%, #d6e6ff, #4f7fd0 60%, #2b4f9a);
  }
  .hours {
    position: absolute; left: 141px; top: 782px; width: 180px; text-align: center;
    font-family: "Roboto Condensed", sans-serif; color: var(--ink);
  }
  .hours-days { font-size: 32px; line-height: 36px; }
  .hours-time { font-size: 23px; font-weight: 700; line-height: 26px; margin-top: 2px; }
  .call {
    position: absolute; left: 92px; top: 924px;
    font-family: "Roboto Condensed", sans-serif; font-size: 27px; color: var(--ink);
  }
  .call strong { font-size: 36px; font-weight: 700; margin-left: 4px; }
  .team {
    position: absolute; left: 57px; top: 984px; width: 339px; height: 190px;
    background: var(--navy); border-radius: 12px;
  }
  .team-title {
    text-align: center; margin-top: 8px;
    font-family: "Roboto Condensed", sans-serif; font-weight: 700;
    font-size: 21px; color: var(--yellow);
  }
  .team-members { display: flex; gap: 10px; padding: 2px 10px 0; }
  .member { flex: 1; text-align: center; }
  .member-name { font-size: 13px; color: var(--white); font-family: "Open Sans", sans-serif; }
  .member-photo {
    margin-top: 6px; height: 114px; border: 2px solid var(--white); border-radius: 4px;
    background: linear-gradient(160deg, #c9b59a, #6f6a6a 55%, #2c3557);
  }
</style>
</head>
<body>
<main class="poster">
  <svg class="poster-shapes" viewBox="0 0 900 1200" width="900" height="1200" aria-hidden="true">
    <defs>
      <radialGradient id="clock-fill" cx="40%" cy="35%" r="70%">
        <stop offset="0" stop-color="#ffffff"/>
        <stop offset="1" stop-color="#bfc2c6"/>
      </radialGradient>
      <radialGradient id="bubble-fill" cx="45%" cy="40%" r="70%">
        <stop offset="0" stop-color="#ffffff"/>
        <stop offset="1" stop-color="#d6d8dc"/>
      </radialGradient>
    </defs>
    <!-- header bands -->
    <path d="M0 0 H900 V280 C750 280 600 278 450 272 C260 264 120 226 0 98 Z" fill="var(--yellow)"/>
    <path d="M0 0 H900 V266 C750 266 600 264 450 258 C260 250 120 212 0 84 Z" fill="var(--orange)"/>
    <path d="M0 0 H900 V244 C750 244 600 242 450 236 C260 228 120 190 0 62 Z" fill="var(--white)"/>
    <!-- lower yellow field -->
    <path d="M0 610 C150 680 300 780 460 880 L460 1200 H0 Z" fill="var(--orange)"/>
    <path d="M0 640 C150 710 300 800 460 900 L460 1200 H0 Z" fill="var(--yellow)"/>
    <path d="M0 700 C120 760 260 860 460 930" fill="none" stroke="var(--orange)" stroke-width="4"/>
    <!-- speech bubble -->
    <path d="M112 600 L70 662 L150 628 Z" fill="#dcdde0" stroke="var(--orange)" stroke-width="5" stroke-linejoin="round"/>
    <ellipse cx="197" cy="530" rx="124" ry="112" fill="url(#bubble-fill)" stroke="var(--orange)" stroke-width="5"/>
    <path d="M108 604 L76 654 L140 622" fill="#dcdde0"/>
    <!-- hours clock -->
    <circle cx="231" cy="826" r="98" fill="var(--orange)"/>
    <circle cx="231" cy="826" r="90" fill="var(--white)"/>
    <circle cx="231" cy="826" r="84" fill="url(#clock-fill)"/>
    <!-- heart frame -->
    <path d="M680 750 C640 680 560 660 505 692 C440 730 432 820 444 1200 H900 V688 C810 672 716 690 680 750 Z" fill="var(--orange)"/>
    <path d="M680 766 C642 700 566 682 516 710 C458 744 452 830 462 1200 H900 V706 C814 692 720 708 680 766 Z" fill="var(--white)"/>
  </svg>

  <svg class="client-photo" viewBox="0 0 900 1200" width="900" height="1200" role="img" aria-label="Photo of a smiling older woman in a white polo shirt inside the gym">
    <defs>
      <linearGradient id="photo-fill" x1="0" y1="0" x2="1" y2="1">
        <stop offset="0" stop-color="#3b3d44"/>
        <stop offset="0.5" stop-color="#b9aea3"/>
        <stop offset="1" stop-color="#eeeae6"/>
      </linearGradient>
    </defs>
    <path d="M680 782 C644 718 572 700 526 726 C474 756 468 840 476 1200 H900 V722 C818 708 722 724 680 782 Z" fill="url(#photo-fill)"/>
  </svg>

  <div class="brand">
    <span class="brand-dot"></span>
    <div class="brand-name">Vital Steps<br>Exercise Physiology Clinic</div>
  </div>
  <p class="clinic-address">Suite 7, 245 Corrigan Road Mackay Q 4740</p>
  <p class="clinic-web">www.tullarowvital.com.au</p>

  <h1 class="headline">Mackay's Over 50's Gym</h1>

  <p class="bubble-text">Exercise with confidence</p>

  <h2 class="question">How old would you be<br>if you didn't know your age?</h2>
  <ul class="benefits">
    <li>Suitable exercise programmes for all medical conditions</li>
    <li>Friendly and non-intimidating environment</li>
    <li>Private health insurance rebates</li>
    <li>University qualified exercise physiologists</li>
  </ul>

  <div class="hours">
    <p class="hours-days">MON - FRI</p>
    <p class="hours-time">8:30 am to<br>6:30 pm</p>
  </div>

  <p class="call">Call Us: <strong>4961 3582</strong></p>

  <section class="team">
    <h3 class="team-title">EXERCISE PHYSIOLOGISTS</h3>
    <div class="team-members">
      <div class="member">
        <p class="member-name">Danielle Prewitt</p>
        <div class="member-photo" role="img" aria-label="Photo of exercise physiologist Danielle Prewitt in the gym"></div>
      </div>
      <div class="member">
        <p class="member-name">Tobias Lindqvist</p>
        <div class="member-photo" role="img" aria-label="Photo of exercise physiologist Tobias Lindqvist in the gym"></div>
      </div>
    </div>
  </section>
</main>
</body>
</html>
```